Tri-Fold Brochure for Substance Abuse Recovery Center

We are looking to freshen up our tri-fold brochure for our recovery facility. Something that helps convey our message of treatment in the great outdoors. I've included a word document with a mock up.

```html
<!DOCTYPE html>
<html lang="en">
<head>
<meta charset="utf-8">
<title>Cedar Hollow Recovery Center – Tri-Fold Brochure</title>
<link rel="stylesheet" href="https://fonts.googleapis.com/css2?family=Lato:ital,wght@0,400;0,700;0,900;1,400&display=swap">
<style>
  :root{
    --blue:#4a86a8;
    --blue-deep:#3f7797;
    --navy:#1f4e6e;
    --orange:#e8912f;
    --ink:#333b42;
    --paper:#ffffff;
    --backdrop:#e9e9e7;
    --tick:#4a6f8a;
  }
  *{box-sizing:border-box;margin:0;padding:0}
  html,body{width:1200px;height:1200px;overflow:hidden}
  body{background:var(--backdrop);font-family:'Lato',sans-serif;color:var(--ink);position:relative}
  .sheet{position:absolute;left:240px;width:720px;height:555px;background:var(--paper);display:flex;box-shadow:0 6px 18px rgba(0,0,0,.18)}
  .sheet--outside{top:30px}
  .sheet--inside{top:615px}
  .panel{position:relative;width:240px;height:555px;overflow:hidden}
  .panel + .panel{border-left:1px solid #eef0f2}
  .panel__text{padding:20px 20px 0 20px}
  .heading{font-size:11.5px;font-weight:700;color:var(--navy);display:inline-block;padding-bottom:2px;border-bottom:1.5px solid var(--orange);margin-bottom:6px}
  .heading--lg{font-size:12.5px}
  .body{font-size:8.3px;line-height:1.34;text-align:justify;margin-bottom:10px}
  .photo{position:absolute;left:0;width:100%}
  .url-band{position:absolute;left:0;bottom:0;width:100%;height:17px;background:var(--blue);color:#fff;font-size:9px;letter-spacing:1.4px;text-align:center;line-height:17px}

  /* mailer panel */
  .panel--mailer{background:var(--blue)}
  .mailer-card{position:absolute;left:11px;top:13px;width:218px;height:527px;background:#fff;border-radius:6px}
  .stamp{position:absolute;left:15px;top:10px;width:55px;height:50px;background:#d9d9d9}
  .photo-strip{position:absolute;left:106px;top:7px;width:102px;display:flex;flex-direction:column;gap:4px}
  .photo-strip .thumb{height:83px}
  .mailer-name{position:absolute;left:62px;top:360px;transform:rotate(-90deg);transform-origin:left top;font-size:9.5px;font-weight:700;color:var(--navy);white-space:nowrap;letter-spacing:.5px}
  .mailer-rule{position:absolute;left:12px;top:380px;width:82px;border-top:1px dotted #bbb}
  .return-address{position:absolute;left:14px;top:515px;transform:rotate(-90deg);transform-origin:left top;font-size:7px;line-height:1.4;color:var(--ink);white-space:nowrap;display:flex;gap:6px}
  .return-address div{display:flex;flex-direction:column}
  .return-address .icon-row{display:flex;align-items:center;gap:3px}
  .return-address svg{width:6px;height:6px}

  /* cover */
  .panel--cover{background:var(--blue)}
  .cover-brand{position:absolute;top:88px;width:100%;text-align:center;color:#fff;font-size:11px;font-weight:700;letter-spacing:1px;line-height:1.4}
  .cover-shape{position:absolute;left:0;top:0;width:240px;height:555px}
  .cover-title{position:absolute;left:0;top:425px;width:100%;text-align:center;line-height:1.08}
  .cover-title .t1{font-size:22px;font-weight:900;color:#fff}
  .cover-title .t2{font-size:22px;font-weight:400;color:var(--orange)}
  .cover-title .t3{font-size:15.5px;font-weight:400;color:#fff;margin-top:5px}
  .cover-title .t4{font-size:15.5px;font-weight:400;color:var(--orange)}
  .cover-url{position:absolute;bottom:10px;width:100%;text-align:center;color:#fff;font-size:9px;letter-spacing:1.4px}

  /* inside */
  .quote{position:relative;margin:15px 18px 12px;border:1.5px solid var(--orange);border-radius:7px;padding:8px 9px 5px;font-size:7.4px;font-style:italic;line-height:1.35}
  .quote__mark{position:absolute;font-size:17px;font-weight:900;color:var(--navy);font-style:normal;line-height:1;background:#fff;padding:0 2px}
  .quote__mark--open{left:6px;top:-9px}
  .quote__mark--close{right:8px;bottom:-11px}
  .quote__by{text-align:right;font-style:normal;font-size:7.4px;margin-top:4px}
  .checklist{list-style:none}
  .checklist li{display:flex;gap:8px;font-size:8.3px;margin-bottom:11.5px;line-height:1.3;align-items:flex-start}
  .checklist svg{flex:0 0 8px;width:8px;height:8px;margin-top:1px}
  .activities{display:grid;grid-template-columns:1fr 1fr;column-gap:8px}
  .activities ul{list-style:none}
  .activities li{display:flex;gap:8px;font-size:8.3px;margin-bottom:10.5px;line-height:1.3;align-items:flex-start;text-transform:uppercase}
  .activities svg{flex:0 0 8px;width:8px;height:8px;margin-top:1px}
</style>
</head>
<body>
<svg width="0" height="0" style="position:absolute">
  <defs>
    <symbol id="tick" viewBox="0 0 10 10">
      <rect x="0.7" y="1.7" width="7.6" height="7.6" fill="none" stroke="var(--tick)" stroke-width="1"/>
      <path d="M2.4 5.3 L4.3 7.2 L9.3 1" fill="none" stroke="var(--tick)" stroke-width="1.3"/>
    </symbol>
  </defs>
</svg>

<!-- OUTSIDE SHEET -->
<section class="sheet sheet--outside">
  <article class="panel panel--campus">
    <div class="panel__text">
      <h2 class="heading">The Campus:</h2>
      <p class="body">Cedar Hollow is nestled in the Ohio Valley with 50 acres of scenic tranquility with lakes and forestry. Located in beautiful mountain setting dynamic master-level clinical staff trained in the most innovative clinical practices.</p>
      <p class="body">Clients will be housed in cabins with spacious accommodations ranging up to 3,900 sq.ft. A picturesque Mountain View villa overlooking the tranquil woods in the valley.</p>
      <p class="body" style="margin-bottom:22px">We provide comfortable housing that is close to the clinical building. We would like you to be at ease with your housing to focus on your journey in recovery.</p>
      <h2 class="heading">The Housing:</h2>
      <p class="body">Our clients reside in spacious, mountain view villas, with many comforts. They even have memory foam mattresses!</p>
    </div>
    <div class="photo" style="top:300px;height:255px;background:linear-gradient(180deg,#fff 0%,#c9d3da 18%,#6e8796 50%,#4b5a5e 80%,#5b5448 100%)" role="img" aria-label="Photo of a couple sitting on rocks by a lake"></div>
    <div class="url-band">www.cedarhollowrecovery.com</div>
  </article>

  <article class="panel panel--mailer">
    <div class="mailer-card">
      <div class="stamp"></div>
      <div class="mailer-name">CEDAR HOLLOW RECOVERY CENTER</div>
      <div class="mailer-rule"></div>
      <div class="return-address">
        <div>
          <span class="icon-row"><svg viewBox="0 0 10 10"><path d="M5 0.5C3 .5 1.8 2 1.8 3.7 1.8 6 5 9.5 5 9.5S8.2 6 8.2 3.7C8.2 2 7 .5 5 .5Z" fill="var(--orange)"/></svg>Cedar Hollow</span>
          <span>12 Birchwood Lane</span>
          <span>Millbrook, West Virginia 26000</span>
        </div>
        <div>
          <span class="icon-row"><svg viewBox="0 0 10 10"><path d="M2 1 L4 1 L5 3.5 L3.8 4.5 Q4.8 6.4 6 7 L7 5.8 L9.5 6.8 L9.5 9 Q4.5 9.5 1 4 Z" fill="var(--orange)"/></svg><b>800-555-0147</b></span>
          <span class="icon-row"><svg viewBox="0 0 10 10"><circle cx="5" cy="5" r="4" fill="none" stroke="var(--orange)" stroke-width="1.4"/></svg>www.cedarhollowrecovery.com</span>
        </div>
        <div>
          <span class="icon-row"><svg viewBox="0 0 10 10"><path d="M5 0.5C3 .5 1.8 2 1.8 3.7 1.8 6 5 9.5 5 9.5S8.2 6 8.2 3.7C8.2 2 7 .5 5 .5Z" fill="var(--orange)"/></svg><b>Street Address</b></span>
          <span>City, ST ZIP Code</span>
        </div>
      </div>
      <div class="photo-strip">
        <div class="thumb" style="background:linear-gradient(180deg,#a9c8e6,#7aa0bf 45%,#4f7a3a)" role="img" aria-label="Campus road under a blue sky"></div>
        <div class="thumb" style="background:linear-gradient(180deg,#c9d6e2,#9aa98a 45%,#6f8a3f)" role="img" aria-label="Lawn and trees on campus"></div>
        <div class="thumb" style="background:linear-gradient(180deg,#b6cbe0,#8a9a6a 50%,#7e6a55)" role="img" aria-label="Cabins among autumn trees"></div>
        <div class="thumb" style="background:linear-gradient(180deg,#3a4b5a,#3d8fc4 55%,#6bb7e0)" role="img" aria-label="Indoor pool"></div>
        <div class="thumb" style="background:linear-gradient(180deg,#e0ddd8,#6a4a3a 55%,#3a2a22)" role="img" aria-label="Lounge with leather furniture"></div>
        <div class="thumb" style="background:linear-gradient(180deg,#b9cde0,#a5b0b5 50%,#5f6e55)" role="img" aria-label="Lake view under clouds"></div>
      </div>
    </div>
  </article>

  <article class="panel panel--cover">
    <div class="photo" style="top:0;height:430px;background:linear-gradient(180deg,#1e4f86 0%,#2b5f95 40%,#3a5d4a 75%,#6f7d3a 100%)" role="img" aria-label="Photo of two hikers helping each other up a grassy slope above a lake"></div>
    <div class="cover-brand">CEDAR HOLLOW<br>RECOVERY CENTER</div>
    <svg class="cover-shape" viewBox="0 0 240 555" aria-hidden="true">
      <polygon points="0,418 130,331 240,428 240,555 0,555" fill="var(--blue)"/>
      <polyline points="0,411 130,322 240,420" fill="none" stroke="var(--orange)" stroke-width="5"/>
    </svg>
    <div class="cover-title">
      <div class="t1">A DESTINATION</div>
      <div class="t2">FOR RECOVERY</div>
      <div class="t3">INSPIRING SOBRIETY</div>
      <div class="t4">&amp; ADVENTURE</div>
    </div>
    <div class="cover-url">www.cedarhollowrecovery.com</div>
  </article>
</section>

<!-- INSIDE SHEET -->
<section class="sheet sheet--inside">
  <article class="panel">
    <blockquote class="quote">
      <span class="quote__mark quote__mark--open">&ldquo;</span>
      Cedar Hollow is not your typical center. Patients don't just sit around all day. There are so many activities that keep them engaged and working on themselves.
      <div class="quote__by">-Marla T.</div>
      <span class="quote__mark quote__mark--close">&rdquo;</span>
    </blockquote>
    <div class="panel__text" style="padding-top:6px">
      <h2 class="heading heading--lg">Who We Are</h2>
      <p class="body">We are a team with a passion for recovery. We are advocates that care about helping find people the right fit for them…even if it isn't with Cedar Hollow.</p>
      <p class="body" style="margin-bottom:18px">However, we feel that Cedar Hollow is the destination recovery center. It allows individuals personal treatment plans, and an unmatched environment.</p>
      <h2 class="heading heading--lg">Our Philosophy</h2>
      <p class="body">At Cedar Hollow, we focus on individualized treatment plans to address mental health, medical and emotional needs. We incorporate the Relapse Prevention Program and treat trauma and co-occurring</p>
    </div>
    <div class="photo" style="top:345px;height:210px;background:linear-gradient(180deg,#fff 0%,#c7d6b6 20%,#8fa66e 55%,#5d6e4a 100%)" role="img" aria-label="Photo of two young hikers walking on a forest trail"></div>
  </article>

  <article class="panel">
    <div class="panel__text">
      <h2 class="heading heading--lg" style="margin-bottom:22px">Relapse Prevention Program</h2>
      <p class="body">We know the statistics. We want them to change. Our Relapse Prevention Program offers an intensive 2 week stabilization program for clients.</p>
      <p class="body">If a patient has been to treatment before, this is the program for them. Our programs have traditional steps to them, with unique individual therapies and recovery options.</p>
    </div>
    <div class="photo" style="left:23px;top:184px;width:193px;height:163px;background:linear-gradient(180deg,#4f6e3a 0%,#6d8a4f 40%,#8a7a6a 70%,#6a7d55 100%)" role="img" aria-label="Photo of a counselor talking with a group outdoors"></div>
    <div class="panel__text" style="position:absolute;top:388px;left:0;right:0">
      <h2 class="heading heading--lg">Improvement</h2>
      <p class="body">We want EVERYONE to walk out of our facility an improved individual. This includes helping improve credit scores, interviewing skills and family foundations.</p>
      <p class="body">Clients learn to reshape their lives with healthy coping skills.</p>
      <p class="body">Our HOPE Program offers Heart Centered Healing: Emotionally Focused Therapy</p>
    </div>
  </article>

  <article class="panel">
    <div class="panel__text" style="padding-top:14px">
      <h2 class="heading heading--lg" style="margin-bottom:14px">Relapse Prevention Program</h2>
      <ul class="checklist">
        <li><svg><use href="#tick"/></svg>A 30 Day Residential Inpatient &amp; Outpatient Treatment.</li>
        <li><svg><use href="#tick"/></svg>Ongoing Recovery Care</li>
        <li><svg><use href="#tick"/></svg>Dialectical Behavioral Therapy</li>
        <li><svg><use href="#tick"/></svg>Emotionally Focused Therapy</li>
        <li><svg><use href="#tick"/></svg>Solution Focused Therapy</li>
        <li><svg><use href="#tick"/></svg>Adventure Therapy</li>
      </ul>
      <h2 class="heading" style="margin-top:4px">Activities</h2>
      <p class="body" style="margin-bottom:10px">These really set us apart!</p>
      <div class="activities">
        <ul>
          <li><svg><use href="#tick"/></svg>Bio Bed</li>
          <li><svg><use href="#tick"/></svg>Acupuncture</li>
          <li><svg><use href="#tick"/></svg>Weekly In-<br>House Salon</li>
          <li><svg><use href="#tick"/></svg>Kayaking</li>
          <li><svg><use href="#tick"/></svg>Hiking</li>
          <li><svg><use href="#tick"/></svg>Fire Pits</li>
        </ul>
        <ul>
          <li><svg><use href="#tick"/></svg>Biking</li>
          <li><svg><use href="#tick"/></svg>Yoga</li>
          <li><svg><use href="#tick"/></svg>Fitness Center</li>
          <li><svg><use href="#tick"/></svg>Pool</li>
          <li><svg><use href="#tick"/></svg>Navigation<br>Ropes Courses</li>
          <li><svg><use href="#tick"/></svg>Zip-Lining</li>
        </ul>
      </div>
    </div>
    <div class="photo" style="top:405px;height:150px;background:linear-gradient(180deg,#fff 0%,#c9d3de 25%,#c8b59a 55%,#e9a94a 75%,#1b1b1b 100%)" role="img" aria-label="Sunset silhouette of a parent and child with bicycles"></div>
  </article>
</section>
</body>
</html>
```